Feedback App to request feedback from colleagues

It’s a small web app to collect feedback from team members. This is the general screen flow but happy for variations to it.

Users logs into application and is able to see the feedback received till date from different colleagues.

At the top right are “Request feedback”, “Respond to Feedback”.

When the user clicks on Request Feedback, there are three options.
Adhoc Feedback
Mid Year Feedback
360 Feedback

Adhoc feedback will open a screen where I can search for colleagues to request feedback from (I can select more than one). There are three pre-defined question that can I edit if needed.

Mid year feedback: same process but questions cannot be edited

360 Feedback - just redirect to another website.

Respond to Feedback - see incoming request and the ability to provide feedback to questions received.

Send Feedback: select a colleague and send adhoc feedback.

Colours to be used are white and red only. Simple design, the app will be embedded in a portal so need for headers etc. think of a mobile view but no need for logo, header bar etc

Colour Codes:
Red: #E60000
White #FFFFFF
Grey: #333333 (Only use if needed e.g. borders, background etc)
Black: #000000

Only the above colours to be used

Number of Pages Required

1 page

Font styles to use
Sans Serif

Colors
EB3D1F
EC4F4E
F09395
F8D3D4
FCEDEE

Requirements
Must have
• Design screens for every page mentioned
Nice to have
• Clean design, use of images and icons
Should not have
• Cluttered design, header

```html
<!DOCTYPE html>
<html lang="en">
<head>
<meta charset="utf-8">
<title>Feedback App Screens</title>
<link href="https://fonts.googleapis.com/css2?family=Roboto:wght@400;500;700&display=swap" rel="stylesheet">
<style>
:root{
  --red-deep:#EB3D1F;
  --red:#EC4F4E;
  --red-soft:#F09395;
  --pink:#F8D3D4;
  --blush:#FCEDEE;
  --white:#FFFFFF;
  --ink:#000000;
  --grey:#333333;
  --muted:#6b6b6b;
  --line:#e4e4e4;
  --page:#f6f6f8;
}
*{box-sizing:border-box;margin:0;padding:0}
html,body{width:1200px;height:1090px;overflow:hidden;background:var(--white);font-family:"Roboto",sans-serif;color:var(--ink)}
.board{position:relative;width:1200px;height:1090px}
.screen{position:absolute;width:368px;height:796px;background:var(--page);transform:scale(.595);transform-origin:0 0;box-shadow:0 0 4px rgba(0,0,0,.18);overflow:hidden}
.screen.tint{background:var(--blush)}
.status{height:16px;background:var(--ink);color:var(--white);font-size:12px;display:flex;justify-content:flex-end;align-items:center;gap:5px;padding-right:8px}
.status svg{display:block}
.topbar{height:44px;background:var(--white);display:flex;align-items:center;justify-content:center;position:relative;font-size:14px;font-weight:700;box-shadow:0 1px 2px rgba(0,0,0,.05)}
.topbar.left{justify-content:flex-start;padding-left:14px}
.topbar .back{position:absolute;left:14px;top:14px}
.topbar .action{position:absolute;right:14px;top:12px}
.art{position:absolute;border-radius:14px}
.art.grey{background:radial-gradient(circle at 50% 55%,#e9a199 0%,#eee 45%,#f2f2f2 70%)}
.art.pinkish{background:radial-gradient(circle at 50% 55%,#d8444d 0%,#f4c6c8 40%,var(--blush) 70%)}
.art.blue{background:radial-gradient(circle at 50% 55%,#4a86d8 0%,#b9d2f0 45%,var(--blush) 75%)}
.card{position:absolute;left:14px;width:340px;background:var(--white);border-radius:6px;box-shadow:0 2px 6px rgba(0,0,0,.08)}
.btn{position:absolute;left:30px;width:307px;height:53px;border-radius:4px;color:var(--white);font-size:17px;font-weight:700;display:flex;align-items:center;justify-content:center;letter-spacing:.3px}
.btn.wide{left:15px;width:338px;top:710px;background:var(--red-deep)}
.opt{position:absolute;left:30px;width:307px;height:53px;border-radius:4px;display:flex;overflow:hidden;color:var(--white);font-size:17px;font-weight:700;letter-spacing:.4px}
.opt .label{flex:1;display:flex;align-items:center;padding-left:29px}
.opt .icon{width:87px;display:flex;align-items:center;justify-content:center}
.opt.adhoc{background:var(--red-soft)}.opt.adhoc .icon{background:#f3a3a4}
.opt.adhoc.active{background:#de7e80}.opt.adhoc.active .icon{background:#e48c8e}
.opt.mid{background:var(--red)}.opt.mid .icon{background:#ee6362}
.opt.full{background:var(--red-deep)}.opt.full .icon{background:#ee5236}
.person{position:absolute;left:14px;width:340px;height:70px;background:var(--white);box-shadow:0 1px 3px rgba(0,0,0,.06)}
.person .avatar{position:absolute;left:9px;top:16px;width:34px;height:34px;border-radius:50%}
.person .name{position:absolute;left:60px;top:16px;font-size:14px;font-weight:500}
.person .sub{position:absolute;left:60px;top:39px;font-size:12px;color:var(--muted)}
.person .check{position:absolute;right:12px;top:15px;width:12px;height:12px;border:1px solid #cfcfcf;border-radius:2px}
.q{position:absolute;left:14px;width:340px;height:95px;background:var(--white);box-shadow:0 1px 3px rgba(0,0,0,.06)}
.q .num{position:absolute;left:7px;top:10px;color:var(--red-deep);font-size:20px;font-weight:500}
.q .text{position:absolute;left:38px;top:10px;width:255px;font-size:14px;line-height:24px}
.q .edit{position:absolute;right:10px;top:12px;width:22px;height:20px;background:var(--red);border-radius:2px;display:flex;align-items:center;justify-content:center}
.field-label{position:absolute;left:31px;font-size:13px;font-weight:700}
.field{position:absolute;left:30px;width:307px;border:1px solid #dcdcdc;border-radius:4px;font-size:12px;color:#8a8a8a;padding:14px 15px;line-height:16px}
.answer-card{position:absolute;left:14px;width:340px;height:225px;background:var(--white);border-radius:6px;box-shadow:0 2px 6px rgba(0,0,0,.06)}
.answer-card .num{position:absolute;left:12px;top:28px;color:var(--red-deep);font-size:18px;font-weight:500}
.answer-card .text{position:absolute;left:38px;top:28px;width:292px;font-size:12.5px;font-weight:700;line-height:16.5px}
.answer-card .field-label{left:17px;top:96px;font-size:13px}
.answer-card .field{left:16px;top:112px;height:91px}
.clip{position:absolute;left:0;right:0;overflow:hidden}
</style>
</head>
<body>
<div class="board">

<!-- Home -->
<section class="screen" style="left:42px;top:37px">
  <div class="status"><svg width="14" height="10"><path d="M1 4a9 9 0 0 1 12 0M3.5 6.5a5.5 5.5 0 0 1 7 0M7 9.5l1.3-1.3a2 2 0 0 0-2.6 0z" stroke="#fff" fill="none" stroke-width="1.4"/></svg><svg width="18" height="10"><path d="M0 10L9 1v9z" fill="#fff"/><rect x="12" y="0" width="5" height="10" fill="#fff"/></svg><span>12:30</span></div>
  <div class="topbar left">Feedback
    <svg class="action" width="14" height="14" viewBox="0 0 14 14"><path d="M4 3.5a5 5 0 1 0 6 0M7 1v6" stroke="#EB3D1F" stroke-width="1.4" fill="none" stroke-linecap="round"/></svg>
  </div>
  <div style="position:absolute;left:0;right:0;top:60px;height:240px;background:#f2f2f2"></div>
  <div class="art grey" role="img" aria-label="Illustration of two colleagues beside a large rating star" style="left:70px;top:80px;width:230px;height:215px"></div>
  <div class="card" style="top:302px;height:200px"></div>
  <div class="btn" style="top:335px;background:var(--red)">Request feedback</div>
  <div class="btn" style="top:418px;background:var(--red-deep)">Respond to Feedback</div>
</section>

<!-- Request Feedback -->
<section class="screen" style="left:336px;top:37px">
  <div class="status"><svg width="14" height="10"><path d="M1 4a9 9 0 0 1 12 0M3.5 6.5a5.5 5.5 0 0 1 7 0M7 9.5l1.3-1.3a2 2 0 0 0-2.6 0z" stroke="#fff" fill="none" stroke-width="1.4"/></svg><svg width="18" height="10"><path d="M0 10L9 1v9z" fill="#fff"/><rect x="12" y="0" width="5" height="10" fill="#fff"/></svg><span>12:30</span></div>
  <div class="topbar">Request Feedback
    <svg class="back" width="16" height="14" viewBox="0 0 16 14"><path d="M15 7H2M7 1.5L1.5 7 7 12.5" stroke="#000" stroke-width="1.6" fill="none"/></svg>
  </div>
  <div style="position:absolute;left:0;right:0;top:60px;height:300px;background:#f2f2f2"></div>
  <div class="art grey" role="img" aria-label="Illustration of a person leaning on a tablet showing rating faces" style="left:55px;top:85px;width:260px;height:200px"></div>
  <div class="card" style="top:311px;height:291px"></div>
  <div class="opt adhoc" style="top:344px"><span class="label">Adhoc Feedback</span><span class="icon"><svg width="34" height="28" viewBox="0 0 34 28"><path d="M2 2h26v16H12l-6 5v-5H2z" stroke="#fff" stroke-width="1.6" fill="none"/><path d="M7 8h16M7 12h10" stroke="#fff" stroke-width="1.4"/><path d="M27 17l1.5 3 3.3.4-2.4 2.3.6 3.3-3-1.6-3 1.6.6-3.3-2.4-2.3 3.3-.4z" stroke="#fff" stroke-width="1.2" fill="none"/></svg></span></div>
  <div class="opt mid" style="top:427px"><span class="label">Mid Year Feedback</span><span class="icon"><svg width="32" height="30" viewBox="0 0 32 30"><circle cx="16" cy="15" r="12" stroke="#fff" stroke-width="1.6" fill="none"/><rect x="3" y="11" width="26" height="8" stroke="#fff" stroke-width="1.4" fill="none"/><text x="16" y="17.5" text-anchor="middle" font-size="6.5" font-family="Roboto,sans-serif" fill="#fff" font-weight="700">YEARS</text></svg></span></div>
  <div class="opt full" style="top:510px"><span class="label">360 Feedback</span><span class="icon"><svg width="30" height="30" viewBox="0 0 30 30"><rect x="3" y="5" width="24" height="22" rx="2" stroke="#fff" stroke-width="1.6" fill="none"/><path d="M9 2v6M21 2v6M3 11h24" stroke="#fff" stroke-width="1.4"/><text x="15" y="23" text-anchor="middle" font-size="8" font-family="Roboto,sans-serif" fill="#fff" font-weight="700">365</text></svg></span></div>
</section>

<!-- Request Feedback (adhoc pressed) -->
<section class="screen" style="left:630px;top:37px">
  <div class="status"><svg width="14" height="10"><path d="M1 4a9 9 0 0 1 12 0M3.5 6.5a5.5 5.5 0 0 1 7 0M7 9.5l1.3-1.3a2 2 0 0 0-2.6 0z" stroke="#fff" fill="none" stroke-width="1.4"/></svg><svg width="18" height="10"><path d="M0 10L9 1v9z" fill="#fff"/><rect x="12" y="0" width="5" height="10" fill="#fff"/></svg><span>12:30</span></div>
  <div class="topbar">Request Feedback
    <svg class="back" width="16" height="14" viewBox="0 0 16 14"><path d="M15 7H2M7 1.5L1.5 7 7 12.5" stroke="#000" stroke-width="1.6" fill="none"/></svg>
  </div>
  <div style="position:absolute;left:0;right:0;top:60px;height:300px;background:#f2f2f2"></div>
  <div class="art grey" role="img" aria-label="Illustration of a person leaning on a tablet showing rating faces" style="left:55px;top:85px;width:260px;height:200px"></div>
  <div class="card" style="top:311px;height:291px"></div>
  <div class="opt adhoc active" style="top:344px"><span class="label">Adhoc Feedback</span><span class="icon"><svg width="40" height="40" viewBox="0 0 40 40"><path d="M5 6h26v16H15l-6 5v-5H5z" stroke="#fff" stroke-width="1.6" fill="none"/><path d="M10 12h16M10 16h10" stroke="#fff" stroke-width="1.4"/><path d="M27 24v10l2-2 2 4 1.5-.8-2-4h3z" fill="#fff" stroke="#000" stroke-width=".8"/></svg></span></div>
  <div class="opt mid" style="top:427px"><span class="label">Mid Year Feedback</span><span class="icon"><svg width="32" height="30" viewBox="0 0 32 30"><circle cx="16" cy="15" r="12" stroke="#fff" stroke-width="1.6" fill="none"/><rect x="3" y="11" width="26" height="8" stroke="#fff" stroke-width="1.4" fill="none"/><text x="16" y="17.5" text-anchor="middle" font-size="6.5" font-family="Roboto,sans-serif" fill="#fff" font-weight="700">YEARS</text></svg></span></div>
  <div class="opt full" style="top:510px"><span class="label">360 Feedback</span><span class="icon"><svg width="30" height="30" viewBox="0 0 30 30"><rect x="3" y="5" width="24" height="22" rx="2" stroke="#fff" stroke-width="1.6" fill="none"/><path d="M9 2v6M21 2v6M3 11h24" stroke="#fff" stroke-width="1.4"/><text x="15" y="23" text-anchor="middle" font-size="8" font-family="Roboto,sans-serif" fill="#fff" font-weight="700">365</text></svg></span></div>
</section>

<!-- Select Profile -->
<section class="screen tint" style="left:923px;top:37px">
  <div class="status"><svg width="14" height="10"><path d="M1 4a9 9 0 0 1 12 0M3.5 6.5a5.5 5.5 0 0 1 7 0M7 9.5l1.3-1.3a2 2 0 0 0-2.6 0z" stroke="#fff" fill="none" stroke-width="1.4"/></svg><svg width="18" height="10"><path d="M0 10L9 1v9z" fill="#fff"/><rect x="12" y="0" width="5" height="10" fill="#fff"/></svg><span>12:30</span></div>
  <div class="topbar">Select Profile
    <svg class="back" width="16" height="14" viewBox="0 0 16 14"><path d="M15 7H2M7 1.5L1.5 7 7 12.5" stroke="#000" stroke-width="1.6" fill="none"/></svg>
  </div>
  <div class="art blue" role="img" aria-label="Illustration of people around a phone showing rated profiles" style="left:70px;top:72px;width:220px;height:155px"></div>
  <div class="clip" style="top:0;height:662px">
    <div class="person" style="top:250px"><span class="avatar" style="background:#c9daf0"></span><span class="name">Carol Smith</span><span class="sub">Lorem Ipsum is simply dummy text</span><svg class="check" viewBox="0 0 12 12"><path d="M2.5 6l2.5 2.5 4.5-5" stroke="#EB3D1F" stroke-width="1.2" fill="none"/></svg></div>
    <div class="person" style="top:340px"><span class="avatar" style="background:#f6c44a"></span><span class="name">Sofia Banks</span><span class="sub">Lorem Ipsum is simply dummy text</span><svg class="check" viewBox="0 0 12 12"><path d="M2.5 6l2.5 2.5 4.5-5" stroke="#EB3D1F" stroke-width="1.2" fill="none"/></svg></div>
    <div class="person" style="top:433px"><span class="avatar" style="background:#e9585a"></span><span class="name">Tomas Cross</span><span class="sub">Lorem Ipsum is simply dummy text</span><svg class="check" viewBox="0 0 12 12"><path d="M2.5 6l2.5 2.5 4.5-5" stroke="#EB3D1F" stroke-width="1.2" fill="none"/></svg></div>
    <div class="person" style="top:523px"><span class="avatar" style="background:#f3cf5a"></span><span class="name">Anita Doe</span><span class="sub">Lorem Ipsum is simply dummy text</span><span class="check"></span></div>
    <div class="person" style="top:615px"><span class="avatar" style="background:#f07a6e"></span><span class="name">Tom parker</span><span class="sub">Lorem Ipsum is simply dummy text</span><span class="check"></span></div>
  </div>
  <div class="btn wide">Continue</div>
</section>

<!-- Questions -->
<section class="screen tint" style="left:42px;top:569px">
  <div class="status"><svg width="14" height="10"><path d="M1 4a9 9 0 0 1 12 0M3.5 6.5a5.5 5.5 0 0 1 7 0M7 9.5l1.3-1.3a2 2 0 0 0-2.6 0z" stroke="#fff" fill="none" stroke-width="1.4"/></svg><svg width="18" height="10"><path d="M0 10L9 1v9z" fill="#fff"/><rect x="12" y="0" width="5" height="10" fill="#fff"/></svg><span>12:30</span></div>
  <div class="topbar">Questions
    <svg class="back" width="16" height="14" viewBox="0 0 16 14"><path d="M15 7H2M7 1.5L1.5 7 7 12.5" stroke="#000" stroke-width="1.6" fill="none"/></svg>
  </div>
  <div class="art pinkish" role="img" aria-label="Illustration of a person thinking beside a large question mark" style="left:95px;top:72px;width:190px;height:185px"></div>
  <div class="q" style="top:278px"><span class="num">01</span><span class="text">Lorem Ipsum is simply dummy text of the printing and typesetting industry. Lorem Ipsum has been ?</span><span class="edit"><svg width="11" height="11" viewBox="0 0 11 11"><path d="M8 1.5h-6.5v8h8v-3M4.5 6.5l5-5" stroke="#fff" stroke-width="1.2" fill="none"/></svg></span></div>
  <div class="q" style="top:390px"><span class="num">02</span><span class="text">Lorem Ipsum is simply dummy text of the printing and typesetting industry. Lorem Ipsum has been ?</span><span class="edit"><svg width="11" height="11" viewBox="0 0 11 11"><path d="M8 1.5h-6.5v8h8v-3M4.5 6.5l5-5" stroke="#fff" stroke-width="1.2" fill="none"/></svg></span></div>
  <div class="q" style="top:505px"><span class="num">03</span><span class="text">Lorem Ipsum is simply dummy text of the printing and typesetting industry. Lorem Ipsum has been ?</span><span class="edit"><svg width="11" height="11" viewBox="0 0 11 11"><path d="M8 1.5h-6.5v8h8v-3M4.5 6.5l5-5" stroke="#fff" stroke-width="1.2" fill="none"/></svg></span></div>
  <div class="btn wide">Submit</div>
</section>

<!-- Questions Edit -->
<section class="screen tint" style="left:336px;top:569px">
  <div class="status"><svg width="14" height="10"><path d="M1 4a9 9 0 0 1 12 0M3.5 6.5a5.5 5.5 0 0 1 7 0M7 9.5l1.3-1.3a2 2 0 0 0-2.6 0z" stroke="#fff" fill="none" stroke-width="1.4"/></svg><svg width="18" height="10"><path d="M0 10L9 1v9z" fill="#fff"/><rect x="12" y="0" width="5" height="10" fill="#fff"/></svg><span>12:30</span></div>
  <div class="topbar">Questions Edit
    <svg class="back" width="16" height="14" viewBox="0 0 16 14"><path d="M15 7H2M7 1.5L1.5 7 7 12.5" stroke="#000" stroke-width="1.6" fill="none"/></svg>
  </div>
  <div class="art pinkish" role="img" aria-label="Illustration of a person thinking beside a large question mark" style="left:95px;top:72px;width:190px;height:185px"></div>
  <div class="card" style="top:284px;height:292px"></div>
  <span class="field-label" style="top:310px">Question&nbsp; No.</span>
  <div class="field" style="top:337px;height:52px;padding-top:19px">01</div>
  <span class="field-label" style="top:407px">Question</span>
  <div class="field" style="top:435px;height:92px;padding-top:20px">Lorem Ipsum is simply dummy text of the printing and typesetting industry. Lorem Ipsum has been ?</div>
  <div class="btn wide">Update</div>
</section>

<!-- Answer -->
<section class="screen tint" style="left:630px;top:569px">
  <div class="status"><svg width="14" height="10"><path d="M1 4a9 9 0 0 1 12 0M3.5 6.5a5.5 5.5 0 0 1 7 0M7 9.5l1.3-1.3a2 2 0 0 0-2.6 0z" stroke="#fff" fill="none" stroke-width="1.4"/></svg><svg width="18" height="10"><path d="M0 10L9 1v9z" fill="#fff"/><rect x="12" y="0" width="5" height="10" fill="#fff"/></svg><span>12:30</span></div>
  <div class="topbar">Answer
    <svg class="back" width="16" height="14" viewBox="0 0 16 14"><path d="M15 7H2M7 1.5L1.5 7 7 12.5" stroke="#000" stroke-width="1.6" fill="none"/></svg>
    <svg class="action" width="20" height="22" viewBox="0 0 20 22"><path d="M4 15V9a6 6 0 0 1 12 0v6l2 2H2zM8 19a2 2 0 0 0 4 0" stroke="#000" stroke-width="1.4" fill="none"/></svg>
  </div>
  <div class="answer-card" style="top:88px"><span class="num">01</span><span class="text">Lorem Ipsum is simply dummy text of the printing and typesetting industry. Lorem Ipsum has been ?</span><span class="field-label">Answer</span><div class="field">Enter Your Answer</div></div>
  <div class="answer-card" style="top:340px"><span class="num">02</span><span class="text">Lorem Ipsum is simply dummy text of the printing and typesetting industry. Lorem Ipsum has been ?</span><span class="field-label">Answer</span><div class="field">Enter Your Answer</div></div>
  <div class="clip" style="top:0;height:686px">
    <div class="answer-card" style="top:585px"><span class="num">03</span><span class="text">Lorem Ipsum is simply dummy text of the printing and typesetting industry. Lorem Ipsum has been ?</span><span class="field-label">Answer</span><div class="field">Enter Your Answer</div></div>
  </div>
  <div class="btn wide">Submit</div>
</section>

</div>
</body>
</html>
```